High end Coffee Roaster needs a Label design for new Blend

We are looking for a label design for a new blend called "Cold Brew Blend". It is a blend of coffee that we use for making cold brew coffee. The blend is sold as the whole bean and ground coffee in a bag as well as pre-brewed ready to drink in a bottle. We would like the label to be elegant but fun and It must include our logo. Please check out or website brightmillroasters.com or social media @brightmillroasters for information on our company and our coffees if you need more ideas on the kind of product we offer and our style.

Requirements
Must have
• Our Company Logo. Creative design.
Should not have
• This project should NOT be a corporate company logo, Please do NOT submit a design for a company logo this is a project for a Label. We already have a logo and we are looking for a design on a label. I have uploaded several examples of what we are looking for. Those examples are from other coffee companies who have cold brew. Those are examples only to give you a better idea of what im looking for. DO NOT COPY THEM.

```html
<!DOCTYPE html>
<html lang="en">
<head>
<meta charset="utf-8">
<title>Bright Mill Roasters – Cold Brew Blend Label</title>
<link rel="stylesheet" href="https://fonts.googleapis.com/css2?family=Big+Shoulders+Display:wght@700;800&family=Oswald:wght@300;500;700&family=Questrial&family=Yellowtail&display=swap">
<style>
  :root {
    --paper: #f5f5f5;
    --plum: #4a2b34;
    --plum-deep: #3b2129;
    --rose-line: #b08a91;
    --gold: #f2b531;
    --gold-deep: #e0a11f;
    --orange: #e2542a;
    --white: #ffffff;
    --ink: #4a3a40;
  }
  * { box-sizing: border-box; margin: 0; padding: 0; }
  html, body { width: 1173px; height: 1200px; overflow: hidden; }
  body { background: var(--paper); position: relative; font-family: "Questrial", sans-serif; }

  .brand-lockup {
    position: absolute; top: 120px; left: 0; width: 100%;
    display: flex; align-items: center; justify-content: center; gap: 22px;
    color: var(--ink);
  }
  .brand-dot { width: 54px; height: 54px; border-radius: 50%; background: var(--gold); flex: none; }
  .brand-name { font-family: "Questrial", sans-serif; font-size: 58px; letter-spacing: 1px; line-height: 1; white-space: nowrap; }
  .brand-sub { display: block; font-size: 22px; letter-spacing: 16px; margin-top: 10px; text-align: center; }

  .label { position: absolute; left: 336px; top: 300px; width: 500px; height: 870px; }
  .label svg { display: block; }

  .t-brand { font-family: "Questrial", sans-serif; fill: var(--white); }
  .t-script { font-family: "Yellowtail", cursive; fill: var(--gold); }
  .t-title { font-family: "Big Shoulders Display", sans-serif; font-weight: 800; fill: var(--white); }
  .t-variant { font-family: "Oswald", sans-serif; font-weight: 300; fill: var(--gold); }
  .t-product { font-family: "Oswald", sans-serif; font-weight: 700; fill: var(--plum-deep); }
  .t-volume { font-family: "Oswald", sans-serif; font-weight: 700; fill: var(--white); }
  .t-producer { font-family: "Oswald", sans-serif; font-weight: 500; fill: var(--white); }
  .t-handle { font-family: "Questrial", sans-serif; fill: var(--white); opacity: 0.9; }
</style>
</head>
<body>
  <header class="brand-lockup">
    <div class="brand-dot"></div>
    <div class="brand-name">BRIGHT MILL<span class="brand-sub">ROASTERS</span></div>
  </header>

  <section class="label">
    <svg viewBox="0 0 500 870" width="500" height="870">
      <path class="label-shape" d="M0 170 H40 V120 Q250 -40 460 120 V170 H500 V870 H0 Z" fill="var(--plum)"/>
      <rect class="label-frame" x="14" y="184" width="472" height="672" fill="none" stroke="var(--rose-line)" stroke-width="2"/>
      <rect class="label-frame" x="22" y="192" width="456" height="656" fill="none" stroke="var(--rose-line)" stroke-width="1"/>

      <g class="label-mark">
        <circle cx="145" cy="104" r="13" fill="var(--gold)"/>
        <text class="t-brand" x="168" y="115" font-size="30" textLength="200" lengthAdjust="spacingAndGlyphs">BRIGHT MILL</text>
        <text class="t-brand" x="268" y="140" font-size="12" text-anchor="middle" textLength="150" lengthAdjust="spacing">ROASTERS</text>
      </g>

      <text class="t-script" x="250" y="255" font-size="66" text-anchor="middle" textLength="300" lengthAdjust="spacingAndGlyphs">Cold Brew</text>
      <text class="t-title" x="250" y="530" font-size="280" text-anchor="middle" textLength="400" lengthAdjust="spacingAndGlyphs">BLEND</text>

      <g class="divider">
        <line x1="70" y1="575" x2="236" y2="575" stroke="var(--gold-deep)" stroke-width="2"/>
        <rect x="244" y="569" width="12" height="12" fill="none" stroke="var(--rose-line)" stroke-width="2" transform="rotate(45 250 575)"/>
        <line x1="264" y1="575" x2="430" y2="575" stroke="var(--gold-deep)" stroke-width="2"/>
      </g>

      <text class="t-variant" x="250" y="640" font-size="50" text-anchor="middle" textLength="330" lengthAdjust="spacingAndGlyphs">ESPRESSO BLEND</text>

      <g class="product-row">
        <rect x="62" y="663" width="300" height="46" fill="var(--gold)"/>
        <text class="t-product" x="212" y="697" font-size="30" text-anchor="middle" textLength="270" lengthAdjust="spacingAndGlyphs">PRIMIUM COFFEE DRINK</text>
        <rect x="370" y="663" width="64" height="46" fill="var(--orange)"/>
        <text class="t-volume" x="402" y="693" font-size="28" text-anchor="middle">16</text>
        <text class="t-volume" x="402" y="704" font-size="9" text-anchor="middle">FL.OZ</text>
      </g>

      <text class="t-producer" x="250" y="752" font-size="17" text-anchor="middle" textLength="330" lengthAdjust="spacingAndGlyphs">BREWED &amp; BOTTLED BY BRIGHTMILLROASTERS</text>
      <text class="t-handle" x="250" y="788" font-size="17" text-anchor="middle">@brightmillroasters</text>
    </svg>
  </section>
</body>
</html>
```